Brochure required for large legal practice

We require a brochure, poster and PowerPoint to be designed to promote our new Employee Benefits Program to our employees. The brochure needs to be modern, clean and corporate. Our target market is solicitors, legal support staff and administration staff based across multiple sites in Queensland, Australia. Logos and brochure/poster content have been attached as well as a detailed brief.

Please note that several photos of our employees have now been uploaded and can be used in this material only.                             

Legal

```html
<!DOCTYPE html>
<html lang="en">
<head>
<meta charset="utf-8">
<title>Health Benefits</title>
<link rel="stylesheet" href="https://fonts.googleapis.com/css2?family=Arimo:wght@400;700&display=swap">
<style>
  :root {
    --ink: #1a1a1a;
    --black: #000000;
    --red: #d71f26;
    --panel-light: #ffffff;
    --panel-mid: #e4e4e4;
    --panel-dark: #bdbdbd;
    --photo-warm-1: #f3e6d6;
    --photo-warm-2: #c9a27c;
    --photo-warm-3: #8a6a4f;
    --photo-green-1: #6f8f4e;
    --photo-green-2: #c9b07a;
  }
  * { box-sizing: border-box; margin: 0; padding: 0; }
  html, body { width: 848px; height: 1200px; overflow: hidden; background: #fff; }
  body { font-family: "Arimo", Arial, sans-serif; color: var(--ink); }
  .page { position: relative; width: 848px; height: 1200px; overflow: hidden;
    background: linear-gradient(90deg, var(--panel-mid) 0%, var(--panel-light) 45%, var(--panel-light) 60%, var(--panel-dark) 100%); }
  .hero-photo { position: absolute; left: 0; top: 0; width: 848px; height: 500px;
    background: radial-gradient(ellipse at 40% 45%, var(--photo-warm-1) 0%, var(--photo-warm-2) 55%, var(--photo-warm-3) 100%); }
  .frame-lines { position: absolute; left: 0; top: 0; width: 848px; height: 1200px; pointer-events: none; }
  .section-title { position: absolute; left: 136px; top: 532px; width: 110px; text-align: right; font-weight: 700; line-height: 1; font-size: 27px; }
  .section-title .accent { display: block; color: var(--red); }
  .section-title .main { display: block; color: var(--black); }
  .intro { position: absolute; left: 264px; top: 536px; width: 524px; font-size: 15.5px; line-height: 1.2; text-align: justify; }
  .tab-heading { position: absolute; left: 76px; top: 648px; width: 330px; height: 34px; }
  .tab-heading svg { position: absolute; inset: 0; }
  .tab-heading span { position: relative; display: block; padding: 7px 0 0 14px; color: #fff; font-weight: 700; font-size: 18.5px; }
  .body-copy { position: absolute; left: 67px; top: 710px; width: 340px; font-size: 16.5px; line-height: 1.26; text-align: justify; letter-spacing: 0.2px; }
  .body-copy p { margin-bottom: 21px; }
  .body-copy p.tight { margin-bottom: 0; }
  .product-list { list-style: none; margin-left: 30px; }
  .product-list li { position: relative; padding-left: 20px; text-align: left; }
  .product-list li::before { content: "›"; position: absolute; left: 0; top: -3px; font-weight: 700; font-size: 20px; }
  .provider-name { position: absolute; left: 460px; top: 640px; color: var(--ink); font-weight: 700; font-size: 40px; line-height: 1; }
  .contact { position: absolute; left: 446px; top: 727px; width: 342px; font-size: 16px; line-height: 1.25; text-align: justify; }
  .contact h3 { font-size: 16.5px; font-weight: 700; }
  .side-photo { position: absolute; left: 452px; top: 846px; width: 332px; height: 260px; border: 3px solid var(--ink);
    background: linear-gradient(160deg, var(--photo-green-1) 0%, var(--photo-green-2) 60%, var(--photo-warm-2) 100%); }
</style>
</head>
<body>
<main class="page">
  <div class="hero-photo" role="img" aria-label="Close-up photo of a smiling young girl resting her head on a parent"></div>

  <svg class="frame-lines" viewBox="0 0 848 1200" aria-hidden="true">
    <rect x="0" y="496" width="848" height="18" fill="var(--black)"/>
    <polyline points="10,505 112,594 136,568" fill="none" stroke="var(--black)" stroke-width="24"/>
    <rect x="0" y="1187" width="848" height="13" fill="var(--black)"/>
    <polyline points="0,1180 64,1110 150,1190" fill="none" stroke="var(--black)" stroke-width="20"/>
  </svg>

  <h1 class="section-title"><span class="accent">Health</span><span class="main">Benefits</span></h1>
  <p class="intro">The health and wellness of our Employees is important to us and we are committed to providing a range of benefits to help our employees lead healthier lives.</p>

  <h2 class="tab-heading">
    <svg viewBox="0 0 330 34" preserveAspectRatio="none" aria-hidden="true">
      <polygon points="0,0 312,0 330,17 312,34 0,34" fill="var(--black)"/>
    </svg>
    <span>Discounted Health Insurance</span>
  </h2>

  <div class="body-copy">
    <p>Employees receive an 8.3% discount on a range of coverage options provided by Vitacare.</p>
    <p class="tight">For Employees that take out both corporate hospital and extras cover, Corporate Ultra Health Cover or any Working Visa Health Insurance within the first 3 months of commencing their employment with Harlow Group or one of its subsidiaries, Vitacare will also waive the 2 &amp; 6 month waiting periods on extras.</p>
    <p class="tight">As Vitacare members, Employees will also receive a 10% discount on the following products:</p>
    <ul class="product-list">
      <li>Travel Insurance</li>
      <li>Pet Insurance</li>
      <li>Life Insurance</li>
      <li>Income Protection Insurance.</li>
    </ul>
  </div>

  <div class="provider-name">Vitacare</div>

  <div class="contact">
    <h3>For further information</h3>
    <p>Employees can call the Vitacare Corporate Hotline on //*// or visit the online member portal at //*//.</p>
  </div>

  <div class="side-photo" role="img" aria-label="Photo of a laughing girl running through a garden sprinkler"></div>
</main>
</body>
</html>
```